Upmarket Artwork, Furniture Retailer needs to Improve existing Vendora Product Template Page

We need to improve an existing design for a Vendora product page. For professional quality we will then like to use the same designer for further work e.g vendora store(Web page)
We need a Web Designer for an exciting new online retailer based in Sydney. Our product is upmarket Scandanavian designed indoor furniture and Rattan outdoor furniture and Modernist Artwork.
Existing Banners,Logo, text, and template can be the same but the Graphic Design need improvement to give the Vendora product page an edge. We like the Green and Brown colours. Attached is teh logo and the extsing Product template

Reason: Thank you everyone for sending through your designs. Soem designs have come in late today and we need some extra time to contact designers. We will be in contact with you to let you know how you went. Kind Regards Delphine

Reason: Still waiting on some redesigns. My apologies for the belated reply. Thank you everyone for sending through great quality work.

Reason: My apologies for the delay. We are waiting on a re design to finalise. Thank you everyone for your patience. Cheers Delphine

Target Market(s)

Upmarket house proud 25-55 professionals

Industry/Entity Type

Graphic Design

Requirements
Must have
• To have an edge to Maximise Buyers
Nice to have
• To use the colours Greens and browns

```html
<!DOCTYPE html>
<html lang="en">
<head>
<meta charset="utf-8">
<title>Lumora – The Fine Art Of Living</title>
<link href="https://fonts.googleapis.com/css2?family=PT+Sans:wght@400;700&display=swap" rel="stylesheet">
<style>
:root{
  --header-bg:#3a3a3a;
  --band-dark:#3c3c3c;
  --sage:#c2caa5;
  --sage-dark:#a9b88a;
  --cream:#faf4e8;
  --ink:#2e2e2e;
  --ink-soft:#3f3f3f;
  --muted:#bcbcbc;
  --nav:#b9b9b9;
  --white:#ffffff;
  --footer-bg:#383838;
  --panel:#333333;
  --rule:#9a9a9a;
  --btn-top:#f6f6f6;
  --btn-bot:#d9d9d9;
}
*{margin:0;padding:0;box-sizing:border-box}
html,body{width:1037px;height:1200px;overflow:hidden;background:var(--cream)}
body{font-family:"PT Sans",sans-serif;color:var(--ink)}
.page{position:relative;width:1020px;height:1180px;transform:scale(1.0167,1.0169);transform-origin:0 0}
.abs{position:absolute}

/* header */
.site-header{position:absolute;left:0;top:0;width:1020px;height:198px;background:var(--header-bg)}
.brand{position:absolute;left:52px;top:67px;width:172px;height:50px;display:flex;align-items:center;gap:10px;padding-left:14px;border-radius:6px;background:#4a4a44}
.brand-mark{width:22px;height:22px;background:var(--sage-dark);border-radius:3px}
.brand-name{font-size:30px;color:var(--white);font-weight:400}
.tagline{position:absolute;right:52px;top:44px;font-size:36px;color:var(--muted)}
.main-nav{position:absolute;right:50px;top:136px;display:flex;gap:6px}
.main-nav a{font-size:19px;color:var(--nav);text-decoration:none;padding:3px 8px}
.main-nav a.active{background:#2c2c2c;border:1px solid #4a4a4a;border-radius:3px;color:#d8d8d8}

/* hero */
.hero{position:absolute;left:0;top:198px;width:1020px;height:308px;background:var(--sage)}
.hero h1{position:absolute;left:50px;top:64px;font-size:25px;font-weight:700;color:var(--ink-soft);text-shadow:1px 1px 1px rgba(255,255,255,.6)}
.hero p{position:absolute;left:50px;top:108px;width:412px;font-size:13.4px;line-height:18.6px;color:#2f2f2f}
.btn-about{position:absolute;left:50px;top:262px;width:130px;height:30px;border:1px solid #8a8a8a;border-radius:4px;background:linear-gradient(var(--btn-top),var(--btn-bot));font-size:14px;color:#333;display:flex;align-items:center;justify-content:center;gap:10px}
.circle-arrow{width:17px;height:17px}
.hero-frame{position:absolute;left:500px;top:51px;width:468px;height:204px;background:#d8dcc4;border-radius:4px;box-shadow:0 2px 6px rgba(0,0,0,.35)}
.hero-art{position:absolute;left:8px;top:7px;width:453px;height:191px;border-radius:3px;background:linear-gradient(170deg,#b8753b 0%,#c98640 35%,#8b3b22 65%,#4a2418 100%)}
.hero-caption{position:absolute;left:8px;bottom:6px;width:453px;height:48px;background:rgba(40,30,25,.45);padding:6px 14px;font-size:10.5px;line-height:11.5px;color:var(--white)}
.band{position:absolute;left:0;top:506px;width:1020px;height:43px;background:var(--band-dark)}

/* content */
.content{position:absolute;left:0;top:549px;width:1020px;height:548px;background:var(--cream)}
.section-title{position:absolute;font-size:16.5px;color:var(--ink);padding-bottom:3px;border-bottom:1px dashed var(--rule)}
.lead{position:absolute;font-size:12px;font-weight:700}
.copy{position:absolute;font-size:11.4px;line-height:12px;color:#333}
.copy.bold{font-weight:700}
.read-more{position:absolute;width:84px;height:21px;border:1px solid #8a8a8a;border-radius:4px;background:linear-gradient(var(--btn-top),var(--btn-bot));font-size:11.5px;color:#444;display:flex;align-items:center;justify-content:center;gap:6px}
.read-more svg{width:13px;height:13px}
.thumb{position:absolute;width:93px;height:122px;background:linear-gradient(180deg,#6d6550 0%,#b69a55 45%,#d9d3c4 75%,#8d7a4e 100%)}
.newsletter{position:absolute;left:698px;top:400px;width:271px;height:119px;background:var(--panel);border-radius:3px;color:var(--white)}
.newsletter h3{position:absolute;left:25px;top:12px;font-size:16px;font-weight:400;display:flex;gap:8px;align-items:center}
.newsletter p{position:absolute;left:25px;top:36px;width:230px;font-size:11.5px;line-height:12px;color:#e6e6e6}
.email-field{position:absolute;left:14px;top:79px;width:157px;height:21px;background:linear-gradient(#ddd,#bdbdbd);font-size:13px;font-style:italic;color:#333;padding:2px 20px}
.subscribe{position:absolute;left:184px;top:79px;width:78px;height:19px;border-radius:3px;background:linear-gradient(#f4f4f4,#cfcfcf);font-size:11.5px;color:#444;text-align:center;line-height:19px}

/* footer */
.site-footer{position:absolute;left:0;top:1097px;width:1020px;height:83px;background:var(--footer-bg)}
.footer-links{position:absolute;left:50px;top:24px;display:grid;grid-template-columns:66px 79px 88px 60px;row-gap:5px;font-size:12.5px;font-weight:700;color:var(--white)}
.social{position:absolute;left:477px;top:34px;display:flex;gap:2px}
.social span{width:16px;height:16px;border-radius:2px}
.footer-brand{position:absolute;right:54px;top:10px;width:103px;height:30px;background:#55584a;border-radius:4px;display:flex;align-items:center;gap:6px;padding-left:8px}
.footer-brand .brand-mark{width:14px;height:14px}
.footer-brand .brand-name{font-size:19px}
.legal{position:absolute;right:50px;top:41px;text-align:right;font-size:12px;line-height:14px;font-weight:700;color:var(--white)}
</style>
</head>
<body>
<div class="page">

<header class="site-header">
  <div class="brand"><span class="brand-mark"></span><span class="brand-name">lumora</span></div>
  <div class="tagline">The Fine Art Of Living</div>
  <nav class="main-nav">
    <a class="active" href="#">Payment</a><a href="#">Delivery</a><a href="#">Warranty</a><a href="#">About Us</a><a href="#">Contact Us</a><a href="#">vendora Store</a>
  </nav>
</header>

<section class="hero">
  <h1>Welcome to Lumora...</h1>
  <p>Lorem ipsum dolor sit amet, consectetur adipisicing elit, sed do eiusmod tempor incididunt ut labore et dolore magna aliqua. Ut enim ad minim veniam, quis nostrud exercitation ullamco laboris nisi ut aliquip ex ea commodo consequat. Duis aute irure dolor in reprehenderit in voluptate velit esse cillum dolore eu fugiat nulla pariatur. Excepteur sint occaecat cupidatat non proident, sunt in culpa qui officia deserunt mollit anim id est laborum.</p>
  <div class="btn-about">About Us
    <svg class="circle-arrow" viewBox="0 0 18 18"><circle cx="9" cy="9" r="7.5" fill="none" stroke="#333" stroke-width="1.5"/><path d="M7 5l5 4-5 4z" fill="#333"/></svg>
  </div>
  <div class="hero-frame">
    <div class="hero-art" role="img" aria-label="Painting of red farmhouses under a warm orange sky"></div>
    <div class="hero-caption">Lorem ipsum dolor sit amet, consectetur adipisicing elit, sed do eiusmod tempor incididunt ut labore et dolore magna aliqua. Ut enim ad minim veniam, quis nostrud exercitation ullamco laboris nisi ut aliquip ex ea commodo consequat. Duis aute irure</div>
  </div>
</section>
<div class="band"></div>

<main class="content">
  <!-- column 1 -->
  <h2 class="section-title" style="left:50px;top:16px">Discription</h2>
  <div class="lead" style="left:53px;top:56px">Lorem ipsum dolor sit amet, consectetur adipisicing.</div>
  <p class="copy" style="left:53px;top:81px;width:275px">&nbsp;sed do eiusmod tempor incididunt ut labore et dolore magna aliqua. Ut enim ad minim veniam, quis nostrud exercitation ullamco laboris nisi ut aliquip ex ea commodo consequat. Duis aute irure dolor in reprehenderit in voluptate velit esse cillum dolore eu fugiat nulla pariatur. Excepteur sint occaecat cupidatat non proident, sunt in culpa qui officia deserunt mollit anim id est laborum.</p>
  <div class="read-more" style="left:221px;top:172px">Read more <svg viewBox="0 0 14 14"><circle cx="7" cy="7" r="6" fill="none" stroke="#333"/><path d="M5.5 4l4 3-4 3z" fill="#333"/></svg></div>

  <h2 class="section-title" style="left:50px;top:206px">Quality Feature</h2>
  <p class="copy" style="left:53px;top:247px;width:270px">Lorem ipsum dolor sit amet, consectetur adipisicing. sed do eiusmod tempor incididunt ut labore et dolore magna aliqua. Ut enim ad minim veniam, quis nostrud exercitation ullamco laboris nisi ut aliquip ex ea commodo consequat. Duis aute irure dolor in reprehenderit in voluptate velit esse cillum dolore eu fugiat nulla pariatur. Excepteur sint occaecat cupidatat non proident, sunt in culpa qui officia deserunt mollit anim id</p>
  <div class="read-more" style="left:221px;top:349px">Read more <svg viewBox="0 0 14 14"><circle cx="7" cy="7" r="6" fill="none" stroke="#333"/><path d="M5.5 4l4 3-4 3z" fill="#333"/></svg></div>

  <h2 class="section-title" style="left:50px;top:395px">Pakage Includes</h2>
  <p class="copy" style="left:53px;top:426px;width:270px">&nbsp;sed do eiusmod tempor incididunt ut labore et dolore magna aliqua. Ut enim ad minim veniam, quis nostrud exercitation ullamco laboris nisi ut aliquip ex ea commodo consequat. Duis aute irure dolor in reprehenderit in voluptate velit esse cillum dolore eu fugiat nulla pariatur. Excepteur sint occaecat cupidatat non proident,</p>
  <div class="read-more" style="left:221px;top:504px">Read more <svg viewBox="0 0 14 14"><circle cx="7" cy="7" r="6" fill="none" stroke="#333"/><path d="M5.5 4l4 3-4 3z" fill="#333"/></svg></div>

  <!-- column 2 -->
  <h2 class="section-title" style="left:395px;top:16px">Featureds Products</h2>
  <div class="thumb" style="left:388px;top:63px" role="img" aria-label="Painting of trees beside a pale building"></div>
  <div class="lead" style="left:492px;top:56px">Indoor Furniture.</div>
  <p class="copy bold" style="left:492px;top:81px;width:165px">&nbsp;sed do eiusmod tempor incididunt ut labore et dolore magna aliqua. Ut enim ad minim veniam, quis nostrud exercitation ullamco laboris nisi ut aliquip ex ea commodo consequat. Duis aute irure dolor in</p>
  <div class="read-more" style="left:568px;top:172px">Read more <svg viewBox="0 0 14 14"><circle cx="7" cy="7" r="6" fill="none" stroke="#333"/><path d="M5.5 4l4 3-4 3z" fill="#333"/></svg></div>

  <h2 class="section-title" style="left:388px;top:206px">Featureds Products</h2>
  <div class="thumb" style="left:388px;top:242px" role="img" aria-label="Painting of trees beside a pale building"></div>
  <div class="lead" style="left:492px;top:235px">Outdoor Furniture.</div>
  <p class="copy" style="left:492px;top:260px;width:165px">&nbsp;sed do eiusmod tempor incididunt ut labore et dolore magna aliqua. Ut enim ad minim veniam, quis nostrud exercitation ullamco laboris nisi ut aliquip ex ea commodo consequat. Duis aute irure dolor in reprehenderit in</p>
  <div class="read-more" style="left:568px;top:350px">Read more <svg viewBox="0 0 14 14"><circle cx="7" cy="7" r="6" fill="none" stroke="#333"/><path d="M5.5 4l4 3-4 3z" fill="#333"/></svg></div>

  <!-- column 3 -->
  <h2 class="section-title" style="left:708px;top:16px">Featureds Products</h2>
  <div class="thumb" style="left:701px;top:63px" role="img" aria-label="Painting of trees beside a pale building"></div>
  <div class="lead" style="left:805px;top:56px">Artwork</div>
  <p class="copy" style="left:805px;top:81px;width:162px">&nbsp;sed do eiusmod tempor incididunt ut labore et dolore magna aliqua. Ut enim ad minim veniam, quis nostrud exercitation ullamco laboris nisi ut aliquip ex ea commodo consequat. Duis aute irure dolor in reprehenderit in</p>
  <div class="read-more" style="left:881px;top:172px">Read more <svg viewBox="0 0 14 14"><circle cx="7" cy="7" r="6" fill="none" stroke="#333"/><path d="M5.5 4l4 3-4 3z" fill="#333"/></svg></div>

  <h2 class="section-title" style="left:700px;top:206px;border-bottom:none">Featureds Products</h2>
  <div class="thumb" style="left:701px;top:242px" role="img" aria-label="Painting of trees beside a pale building"></div>
  <div class="lead" style="left:805px;top:235px">Special</div>
  <p class="copy" style="left:805px;top:260px;width:162px">&nbsp;sed do eiusmod tempor incididunt ut labore et dolore magna aliqua. Ut enim ad minim veniam, quis nostrud exercitation ullamco laboris nisi ut aliquip ex ea commodo consequat. Duis aute irure dolor in reprehenderit in</p>
  <div class="read-more" style="left:881px;top:350px">Read more <svg viewBox="0 0 14 14"><circle cx="7" cy="7" r="6" fill="none" stroke="#333"/><path d="M5.5 4l4 3-4 3z" fill="#333"/></svg></div>

  <div class="newsletter">
    <h3>Newsletters <svg width="22" height="16" viewBox="0 0 22 16"><rect x="1" y="1" width="20" height="14" fill="none" stroke="#fff" stroke-width="1.2"/><path d="M1 1l10 8 10-8" fill="none" stroke="#fff" stroke-width="1.2"/></svg></h3>
    <p>Subscribe to get latest updates delivereright to your inbox. We do not spam.</p>
    <div class="email-field">name@email.com</div>
    <div class="subscribe">Subscribe</div>
  </div>
</main>

<footer class="site-footer">
  <div class="footer-links">
    <span>Home</span><span>Delivery</span><span>Warranty</span><span>Payment</span>
    <span>About Us</span><span>Comntat US</span><span>Privacy Setting</span><span>Feedback</span>
  </div>
  <div class="social">
    <span style="background:#e8892c"></span><span style="background:#e8a02c"></span><span style="background:#3b5ba0"></span><span style="background:#d8d0b0"></span><span style="background:#4aa3df"></span><span style="background:#d64a8c"></span>
  </div>
  <div class="footer-brand"><span class="brand-mark"></span><span class="brand-name">lumora</span></div>
  <div class="legal">copyright @ 2012 Lumora.<br>All right reserver | Privacy Policy</div>
</footer>

</div>
</body>
</html>
```